Business Card design for an International Import Export House

We need a Business Card design for our import export business. We trade in Minerals, Metals, Rice, Sugar, Steel etc.. The design should be minimalistic. It may or may not contain the physical address. In case you want to include the physical address - 418 Verandah Heights, Marlow Sector 9, Gurgaon, Haryana, India, 122009.

Target Market(s)

Steel Mills or Steel Plants, Factories, Mining businesses, Industrial houses, Government Agencies

Industry/Entity Type

Importer

Contact Information for Business Card

Business Name - Varrow Overseas

Font styles to use
Other font styles liked:
• montserrat

Requirements
Must have
• Ravi Kandola - President
• www.varrowoverseas.com
• ravi@varrowoverseas.com
• +91-987-654-3217
Nice to have
• worldwide suppliers of ores

```html
<!DOCTYPE html>
<html lang="en">
<head>
<meta charset="utf-8">
<title>Varrow Overseas – Business Card</title>
<link rel="stylesheet" href="https://fonts.googleapis.com/css2?family=Montserrat:wght@400;500;600;700&display=swap">
<style>
  :root {
    --bg: #d9dadc;
    --card-dark: #1d1e20;
    --card-light: #ffffff;
    --teal: #1f7590;
    --teal-light: #3f8aa6;
    --text-light: #f2f2f2;
    --text-muted: #c9cbcd;
    --map-dark: #26282b;
    --map-light: #e6e6e6;
  }
  * { box-sizing: border-box; margin: 0; padding: 0; }
  html, body {
    width: 1200px; height: 834px; overflow: hidden;
    background: var(--bg);
    font-family: "Montserrat", sans-serif;
  }
  .sheet {
    position: relative; width: 1200px; height: 834px;
    display: flex; flex-direction: column; align-items: center; justify-content: center; gap: 34px;
  }
  .card {
    position: relative; width: 640px; height: 366px; overflow: hidden;
    background: var(--card-dark);
    box-shadow: 0 10px 28px rgba(0,0,0,.25);
  }

  /* Front */
  .front-map {
    position: absolute; left: 90px; top: 40px; width: 460px; height: 240px;
    border-radius: 40% 45% 35% 40%;
    background: radial-gradient(ellipse at center, var(--map-dark) 0%, rgba(38,40,43,0) 70%);
  }
  .wordmark {
    position: absolute; display: flex; align-items: center; gap: 12px;
    font-weight: 700; text-transform: uppercase; letter-spacing: .5px; white-space: nowrap;
  }
  .wordmark .dot {
    flex: none; width: 18px; height: 18px; border-radius: 50%; background: var(--teal-light);
  }
  .front .wordmark {
    left: 0; right: 0; top: 160px; justify-content: center;
    font-size: 30px; color: var(--text-light);
  }
  .front-band {
    position: absolute; left: 0; bottom: 0; width: 100%; height: 22px; background: var(--teal);
  }
  .front-band::before {
    content: ""; position: absolute; left: 286px; top: -14px;
    border-left: 16px solid transparent; border-right: 16px solid transparent;
    border-bottom: 14px solid var(--teal);
  }

  /* Back */
  .back-panel {
    position: absolute; left: 0; top: 0; width: 250px; height: 100%; background: var(--card-light);
  }
  .back-map {
    position: absolute; left: 20px; top: 60px; width: 210px; height: 250px;
    border-radius: 45% 40% 50% 35%;
    background: radial-gradient(ellipse at center, var(--map-light) 0%, rgba(230,230,230,0) 72%);
  }
  .back .wordmark {
    left: 0; width: 250px; top: 170px; justify-content: center; gap: 10px;
    font-size: 16px; color: var(--teal);
  }
  .back .wordmark .dot { width: 12px; height: 12px; background: var(--teal); }
  .back-strip {
    position: absolute; left: 250px; top: 0; width: 22px; height: 100%; background: var(--teal);
  }
  .back-strip::before {
    content: ""; position: absolute; left: -14px; top: 138px;
    border-top: 16px solid transparent; border-bottom: 16px solid transparent;
    border-right: 14px solid var(--teal);
  }
  .contact {
    position: absolute; left: 306px; top: 62px; right: 20px; color: var(--text-light);
  }
  .contact-name { font-size: 26px; font-weight: 700; }
  .contact-title { font-size: 15px; font-weight: 500; color: var(--teal-light); margin-top: 4px; }
  .contact-rule { width: 136px; height: 2px; background: var(--text-light); margin: 12px 0 22px; }
  .contact-list { list-style: none; display: flex; flex-direction: column; gap: 10px; }
  .contact-item { display: flex; align-items: flex-start; gap: 12px; font-size: 14px; color: var(--text-muted); line-height: 1.35; }
  .contact-item svg { flex: none; width: 15px; height: 15px; margin-top: 2px; fill: var(--teal-light); }
</style>
</head>
<body>
<main class="sheet">

  <section class="card front" aria-label="Card front">
    <div class="front-map" role="img" aria-label="Faint dotted world map"></div>
    <div class="wordmark"><span class="dot"></span>Varrow Overseas</div>
    <div class="front-band"></div>
  </section>

  <section class="card back" aria-label="Card back">
    <div class="back-panel">
      <div class="back-map" role="img" aria-label="Light grey dotted world map"></div>
      <div class="wordmark"><span class="dot"></span>Varrow Overseas</div>
    </div>
    <div class="back-strip"></div>
    <div class="contact">
      <h1 class="contact-name">Ravi Kandola</h1>
      <p class="contact-title">President</p>
      <div class="contact-rule"></div>
      <ul class="contact-list">
        <li class="contact-item">
          <svg viewBox="0 0 16 16" aria-hidden="true"><path d="M3.6 1.2l2.3 2.6-1.3 1.8c.9 2 2.5 3.6 4.6 4.6l1.8-1.3 2.6 2.3-1.4 2.2C6.6 13.4 2.6 9.4 1.4 3.6z"/></svg>
          <span>+91-987-654-3217</span>
        </li>
        <li class="contact-item">
          <svg viewBox="0 0 16 16" aria-hidden="true"><path d="M8 1a7 7 0 100 14A7 7 0 008 1zm0 1.6c.8.9 1.4 2.3 1.6 4.1H6.4C6.6 4.9 7.2 3.5 8 2.6zM2.7 8.3h2.2c.1 1.8.6 3.4 1.3 4.5a5.4 5.4 0 01-3.5-4.5zm0-1.6a5.4 5.4 0 013.5-4.5c-.7 1.1-1.2 2.7-1.3 4.5zm5.3 6.7c-.8-.9-1.4-2.3-1.6-5.1h3.2c-.2 2.8-.8 4.2-1.6 5.1zm1.8-.6c.7-1.1 1.2-2.7 1.3-4.5h2.2a5.4 5.4 0 01-3.5 4.5zm1.3-6.1c-.1-1.8-.6-3.4-1.3-4.5a5.4 5.4 0 013.5 4.5z"/></svg>
          <span>www.varrowoverseas.com</span>
        </li>
        <li class="contact-item">
          <svg viewBox="0 0 16 16" aria-hidden="true"><path d="M1 3h14v10H1zm1.6 1.4v.3L8 8.6l5.4-3.9v-.3zM2.6 6.6v5h10.8v-5L8 10.5z"/></svg>
          <span>ravi@varrowoverseas.com</span>
        </li>
        <li class="contact-item">
          <svg viewBox="0 0 16 16" aria-hidden="true"><path d="M8 1a5 5 0 00-5 5c0 3.6 5 9 5 9s5-5.4 5-9a5 5 0 00-5-5zm0 7a2 2 0 110-4 2 2 0 010 4z"/></svg>
          <span>418 Verandah Heights, Marlow Sector 9<br>Gurgaon, Haryana, India, 122009</span>
        </li>
      </ul>
    </div>
  </section>

</main>
</body>
</html>
```